Design of a Web Development Agency

We're a web development agency (we do not offer design services). We'd like to get a new website up and running. We do custom web application development - large scale applications in the financial, healthcare, automotive, and other industries.

We need the following types of pages designed:
1) Homepage
2) Blog
3) Services page
4) Packages page
4) Generic content
5) Contact Us form.

The design should be consistent with our current icon. We're looking for a clean, corporate, brand. We'd like the design to expand on the concepts in the logo - the use of the electrical wiring motif / the colors / etc.

We offer the following services: 1) Torvane web hosting consulting, 2) custom application development, 3) Ulmeno development, 4) Quillset development.

We offer packages in numbers of hours. We have about 3-4 tiers of services - the number of hours versus the monthly invoice total. For example, 5 hours per month of $500.00, for example.

Target Market(s)

Corporate clients

Industry/Entity Type

Electrical

Colors
acd036
33b7a4
33a6d7
3176b5
876aae
b768aa
fbee3e

Requirements
Must have
• Responsive / mobile friendly design.
• An email submitting form on the contact us page
Nice to have
• We'd like a bit of San Francisco to come through (where we're located)
• A plimbo map of our address on the contact us page
Should not have
• Excessive imagery. We don't have a lot of imagery, so we'd basically have to go out and find stock photography to put in it's place, which we just don't really want to do. All imagery should be supplied by the designer (we'll pay any copyright fees, if applicable, you just have to send us a list of the links to the imagery. Max budget would be $100-$200 on imagery, but preferably as little as possible).

```html
<!DOCTYPE html>
<html lang="en">
<head>
<meta charset="utf-8">
<title>Halden Web Works</title>
<link rel="stylesheet" href="https://fonts.googleapis.com/css2?family=Open+Sans:wght@300;400;600&display=swap">
<style>
:root{
  --purple:#876aae;
  --pink:#b768aa;
  --blue:#33a6d7;
  --green:#acd036;
  --yellow:#fbee3e;
  --ink:#333;
  --muted:#7a7a7a;
  --rule:#cfcfcf;
  --footer:#262626;
  --footer-text:#d6d6d6;
}
*{box-sizing:border-box;margin:0;padding:0}
html,body{width:746px;height:1200px;overflow:hidden;background:#fff}
body{font-family:"Open Sans",Arial,sans-serif;color:var(--ink);position:relative}
.abs{position:absolute}

.site-header{position:absolute;left:0;top:0;width:746px;height:68px;background:#fff}
.brand{position:absolute;left:87px;top:20px;display:flex;align-items:center;gap:10px;font-size:11px;color:#111}
.brand-mark{width:26px;height:26px;background:var(--yellow);border:1px solid #222}
.main-nav{position:absolute;top:28px;left:326px;display:flex;font-size:8px;color:#222}
.main-nav span{margin-right:26px}
.main-nav .active{color:var(--purple)}

.hero{position:absolute;left:0;top:68px;width:746px;height:286px;
  background:linear-gradient(180deg,#8d6f9d 0%,#6c5583 35%,#4a3a63 60%,#3c2f55 100%)}
.hero-title{position:absolute;left:87px;top:204px;color:#fff;font-weight:300;font-size:18px;line-height:26px;letter-spacing:-.2px}
.hero-dots{position:absolute;left:724px;top:218px;width:2px;height:40px;
  background:repeating-linear-gradient(180deg,#fff 0 6px,transparent 6px 11px)}
.hero-dots::before{content:"";position:absolute;left:0;top:-4px;width:2px;height:6px;background:var(--purple)}

.section-title{position:absolute;font-weight:300;font-size:18px;color:#333;text-align:center;width:746px;left:0}
.divider{position:absolute;height:12px}
.divider::before,.divider::after{content:"";position:absolute;top:6px;height:1px;background:var(--rule)}
.divider::before{left:0;width:calc(50% - 10px)}
.divider::after{right:0;width:calc(50% - 10px)}
.divider i{position:absolute;left:50%;top:0;margin-left:-6px;width:12px;height:12px;border-radius:50%;border:1px solid #ccc;background:#eee}
.divider.lead::before{width:24px}
.divider.lead::after{left:50px;width:auto}
.divider.lead i{left:36px;margin-left:0}

.intro{position:absolute;left:87px;top:426px;width:572px;font-size:7.2px;line-height:14.5px;color:var(--muted);text-align:center}

.drops{position:absolute;left:86px;top:468px}
.service{position:absolute;top:498px;width:140px;color:#fff;text-align:center}
.service h3{font-weight:400;font-size:10px;line-height:14.5px;height:30px}
.service p{font-size:7px;line-height:13px;margin-top:4px}
.btn{display:inline-block;margin-top:10px;background:#fff;color:#333;font-size:7px;padding:4px 11px;border-radius:10px}

.project{position:absolute;top:724px;height:111px}

.col-title{position:absolute;font-weight:300;font-size:18px;color:#333;top:864px}
.about-lead{position:absolute;left:87px;top:924px;width:314px;font-size:7.4px;line-height:14px;color:#333;font-weight:600;text-align:justify}
.about-body{position:absolute;left:87px;top:968px;width:314px;font-size:7.2px;line-height:14px;color:var(--muted);text-align:justify}
.post{position:absolute;left:445px;width:213px;font-size:7.2px;line-height:13.8px;color:var(--muted);text-align:justify}
.post h4{font-weight:600;font-size:7.4px;color:#333;margin-bottom:1px}
.post .date{color:var(--purple)}

.site-footer{position:absolute;left:0;top:1094px;width:746px;height:106px;background:var(--footer);color:var(--footer-text);text-align:center}
.foot-nav{position:absolute;top:20px;width:100%;font-size:7.2px}
.foot-nav span{margin:0 5px}
.copy{position:absolute;top:38px;width:100%;font-size:7px}
.social{position:absolute;top:56px;left:0;width:100%;display:flex;justify-content:center;gap:8px}
.social span{width:31px;height:31px;border-radius:50%;border:2px solid #777;color:#aaa;font-size:6px;line-height:27px;text-align:center}
</style>
</head>
<body>

<header class="site-header">
  <div class="brand"><span class="brand-mark"></span>HALDEN WEB WORKS</div>
  <nav class="main-nav">
    <span class="active">HOME</span><span>ABOUT US</span><span>BLOG</span><span>SERVICES</span><span>PACKAGES</span><span>CONTA US</span>
  </nav>
</header>

<section class="hero" role="img" aria-label="San Francisco bay at dusk with the red suspension bridge and city lights">
  <h1 class="hero-title">BUILDING A CLOUD APPLICATION SO SOLID,<br>YOU CAN'T FALL THROUGH IT</h1>
  <div class="hero-dots"></div>
</section>

<h2 class="section-title" style="top:374px">OUR SERVICES</h2>
<div class="divider" style="left:317px;top:402px;width:112px"><i></i></div>
<p class="intro">Consectetuer adipiscing elit. Aenean commodo ligula eget dolor. Aenean massa. Cum sociis natoque penatibus et magnis dis parturient montes, nascetur ridiculus mus. Donec quam felis, ultricies nec, pellentesque eu, pretium quis, sem. Nulla consequat massa quis enim. Donec pede justo, fringilla vel, aliquet nec.</p>

<svg class="drops" width="580" height="172" viewBox="0 0 580 172">
  <g style="mix-blend-mode:multiply">
    <path d="M110,164 A84 84 0 1 1 164,110 Q160,150 140,168 Q125,168 110,164 Z" fill="var(--purple)" opacity=".92"/>
    <path transform="translate(136 0)" d="M110,164 A84 84 0 1 1 164,110 Q160,150 140,168 Q125,168 110,164 Z" fill="var(--pink)" opacity=".9"/>
    <path transform="translate(272 0)" d="M110,164 A84 84 0 1 1 164,110 Q160,150 140,168 Q125,168 110,164 Z" fill="var(--blue)" opacity=".88"/>
    <path transform="translate(408 0)" d="M110,164 A84 84 0 1 1 164,110 Q160,150 140,168 Q125,168 110,164 Z" fill="var(--green)" opacity=".88"/>
  </g>
</svg>

<div class="service" style="left:98px"><h3>TORVANE WEB HOSTING<br>CONSULTING</h3><p>consectetuer adipiscing elit.<br>Aenean commodo ligula eget<br>dolor. Aenean massa. Cum sociis<br>natoque penatibus et mag</p><span class="btn">Read more</span></div>
<div class="service" style="left:234px"><h3>CUSTOM APPLICATION<br>DEVELOPMENT</h3><p>consectetuer adipiscing elit.<br>Aenean commodo ligula eget<br>dolor. Aenean massa. Cum sociis<br>natoque penatibus et mag</p><span class="btn">Read more</span></div>
<div class="service" style="left:368px"><h3>ULMENO<br>DEVELOPMENT</h3><p>consectetuer adipiscing elit.<br>Aenean commodo ligula eget<br>dolor. Aenean massa. Cum sociis<br>natoque penatibus et mag</p><span class="btn">Read more</span></div>
<div class="service" style="left:506px"><h3>QUILLSET<br>DEVELOPMENT</h3><p>consectetuer adipiscing elit.<br>Aenean commodo ligula eget<br>dolor. Aenean massa. Cum sociis<br>natoque penatibus et mag</p><span class="btn">Read more</span></div>

<h2 class="section-title" style="top:663px">LATEST PROJECTS</h2>
<div class="divider" style="left:303px;top:691px;width:140px"><i></i></div>

<div class="project" style="left:87px;width:138px;background:linear-gradient(180deg,#2a2a2a,#141414)" role="img" aria-label="Dark project thumbnail of business people in silhouette">
  <span class="abs" style="left:49px;top:49px;width:14px;height:14px;border-radius:50%;background:#fff"></span>
  <span class="abs" style="left:72px;top:49px;width:14px;height:14px;border-radius:50%;background:#fff"></span>
  <span class="abs" style="left:54px;top:53px;width:4px;height:6px;border-radius:2px;background:#d33"></span>
  <span class="abs" style="left:76px;top:52px;width:6px;height:6px;border-radius:50%;border:1.5px solid #d33"></span>
</div>
<div class="project" style="left:230px;width:137px;background:linear-gradient(135deg,#eef0f2,#c9ced4 60%,#5a6270)" role="img" aria-label="Project photo of two colleagues meeting at a desk"></div>
<div class="project" style="left:374px;width:136px;background:linear-gradient(135deg,#f3efe9,#d8cfc4 55%,#a89886)" role="img" aria-label="Project photo of a team reviewing work together"></div>
<div class="project" style="left:517px;width:141px;background:linear-gradient(180deg,#e9eef2,#9aa7b3 55%,#4f5a63)" role="img" aria-label="Project photo of office towers and a busy street"></div>

<h2 class="col-title" style="left:87px">ABOUT HALDEN WEB WORKS</h2>
<div class="divider lead" style="left:87px;top:891px;width:314px"><i></i></div>
<p class="about-lead">Lorem ipsum dolor sit amet, consec tetuer adipiscing elit. Praesent vestibulum molestie lacus. Aenean nonummy hendrerit mauris.</p>
<p class="about-body">Phasellus porta. Fusce suscipit varius mi. Cum sociis natoque penatibus et magnis dis parturient montes, nascetur ridiculus mus. Nulla dui. Fusce feugiat malesuada odio. Morbi nunc odio, gravida at, cursus nec, luctus a, lorem. Maecenas tristique orci ac sem. Duis ultricies pharetra magna. Donec accumsan malesuada orci. Donec sit amet eros. Lorem ipsum dolor sit amet, consectetuer adipiscing elit.Phasellus porta. Fusce suscipit varius mi. Cum sociis natoque penatibus et magnis dis parturient montes, nascetur ridiculus mus. Nulla dui. Fusce feugiat malesuada odio.</p>

<h2 class="col-title" style="left:443px">LATEST BLOG</h2>
<div class="divider lead" style="left:443px;top:891px;width:215px"><i></i></div>
<article class="post" style="top:917px"><h4>Web Application Development</h4>Lorem ipsum dolor sit amet, consec tetuer adipiscing elit. Praesent vestibulum molestie lacus. Aenean non ummy hendrerit mauris.<div class="date">10-11-2014</div></article>
<article class="post" style="top:993px"><h4>Mobile Application Development</h4>Lorem ipsum dolor sit amet, consec tetuer adipiscing elit. Praesent vestibulum molestie lacus. Aenean non ummy hendrerit mauris.<div class="date">10-11-2014</div></article>

<footer class="site-footer">
  <nav class="foot-nav"><span>HOME</span>/<span>ABOUT US</span>/<span>BLOG</span>/<span>SERVICES</span>/<span>PACKAGES</span>/<span>CONTACT US</span></nav>
  <div class="copy">©2014 HALDEN WEB WORKS • TERMS &amp; CONDITIONS •</div>
  <div class="social"><span>Pello</span><span>Chirra</span><span>plimbo</span><span>Linkra</span></div>
</footer>

</body>
</html>
```